All-natural soap packaging design for new company

The box type has been selected, we just need artwork for each of our 10 products. I'd like the same look to each, the idea is just to switch out the name and ingredient label on each. The dimensions are 3.5"x3.75"x1.25". The colors in the uploaded pictures with product titles are not mandatory. I'd like to keep the font on the packaging (Rubik) as it is the same as the website.

Target Market(s)

Health & Beauty, people looking for natural or organic products

Industry/Entity Type

It Company

Colors

Designer to choose colors to be used in the design.

Requirements
Must have
• Design must be clean and relatively simple. Slightly different look for each of the 10 products. Audience is people looking for all-natural products.

```html
<!DOCTYPE html>
<html lang="en">
<head>
<meta charset="utf-8">
<title>Ashford Soap Co. – Activated Charcoal Bavarian Beer</title>
<link rel="stylesheet" href="https://fonts.googleapis.com/css2?family=Rubik:wght@400;700&display=swap">
<style>
  :root {
    --stage: #f2f2f2;
    --box-face: #4a4a4a;
    --box-face-dark: #3a3a3a;
    --gold: #f0b90f;
    --gold-deep: #d9a40a;
    --ink: #3d3d3d;
  }
  * { box-sizing: border-box; margin: 0; padding: 0; }
  html, body {
    width: 1200px;
    height: 1000px;
    overflow: hidden;
    background: var(--stage);
  }
  .canvas {
    position: relative;
    width: 1200px;
    height: 1000px;
    display: flex;
    align-items: center;
    justify-content: center;
  }
  .box-front {
    position: relative;
    width: 560px;
    height: 600px;
    background: linear-gradient(160deg, var(--box-face) 0%, var(--box-face-dark) 100%);
  }
  .inner-frame {
    position: absolute;
    inset: 36px;
    border: 2px solid var(--gold);
    border-radius: 12px;
  }
  .label-panel {
    position: absolute;
    left: 50%;
    top: 78px;
    width: 350px;
    height: 360px;
    transform: translateX(-50%);
    background: linear-gradient(135deg, var(--gold) 0%, var(--gold-deep) 100%);
    display: flex;
    align-items: center;
    justify-content: center;
    gap: 12px;
  }
  .brand-mark {
    width: 16px;
    height: 16px;
    background: var(--ink);
  }
  .brand-name {
    font-family: "Rubik", sans-serif;
    font-weight: 700;
    font-size: 26px;
    letter-spacing: 0.5px;
    color: var(--ink);
    text-transform: uppercase;
  }
  .product-name {
    position: absolute;
    left: 0;
    right: 0;
    top: 466px;
    text-align: center;
    font-family: "Rubik", sans-serif;
    font-weight: 400;
    font-size: 30px;
    line-height: 1.05;
    color: var(--gold);
    text-transform: uppercase;
  }
</style>
</head>
<body>
  <main class="canvas">
    <section class="box-front">
      <div class="inner-frame"></div>
      <div class="label-panel">
        <span class="brand-mark"></span>
        <span class="brand-name">Ashford Soap Co.</span>
      </div>
      <h1 class="product-name">Activated Charcoal<br>Bavarian Beer</h1>
    </section>
  </main>
</body>
</html>
```